Flyer Design Project for our Parenting Psychologists at the Wellmind Counselling Centre

At the Wellmind Counselling Centre we have expert Parenting Psychologists.

Parenting Psychologists provide practical, step by step assistance to parents who are struggling with their children's behavioural and emotional problems.

We need a DL size brochure that will be appealing to parents. The brochure will be on show in schools, kindergartens and GP clinics.

In terms of style it will be in line with our website and stationery that I will attach.

www.wellmindcounsellingcentre.com.au

Hi Everyone,
Thanks for putting forward your proposals, there are a couple there that I am very interested in. I am looking to see if there is a way that I can change my brief to guaranteed as I am definitely going to be using one of the designs for sure.
I have emailed ArtForge and as soon as I get an answer I will change it if I can.
If anyone out there already knows the answer please let me know :-)
Thanks,
Marcie.

Hi Again,

I worked it out myself!!

I have now changed this to a committed project.

Kind regards,
Marcie.

Reason: I have 46 designs now and need more time to work out which is best!

Target Market(s)

The target will be educated professional parents motivated to get professional help. And doctors and teachers who will pass on the brochures 2 parents

Industry/Entity Type

Health

Requirements
Must have
• I want one DL size brochure. Back and front.

We need text (below) and our contact details. Our logo.

6352 1840
Suite 1, 2087 Tamworth Rd, Tamworth North 3118

Text:
Parents want the best for their kids. They want kids that are happy, healthy and well behaved.

So why is it so hard? Parents of toddlers, primary schoolers and teenagers alike say that they are frustrated by constant nagging, bribing and yelling, they don't know what to try next. Some parents worry that their children are unhappy. Struggling at school, not making friends or coping with bigger problems.

The good news is that getting your children to behave more co-operatively doesn't need to be difficult or mysterious. We all know that kids don't come with manuals, but there are skills every parent can learn to make parenting easier. In a few sessions with a Parenting Psychologist, you will receive step by step guidance in how to talk to your children in a way that will be much more effective getting them to behave in a respectful and co-operative way around the home and in public. You will learn how to help your child cope with problems they are going through. They can help you reconnect with your kids so you can enjoy being a parent again.

Nice to have
• Themes consistent with our website
and letterhead, business cards. I will attach these.
Should not have
• I don't want it to look too cluttered so if the text I have provided up above looks too crowded then I will edit it.

```html
<!DOCTYPE html>
<html lang="en">
<head>
<meta charset="utf-8">
<title>Wellmind Counselling Centre – Parenting Flyer</title>
<link rel="stylesheet" href="https://fonts.googleapis.com/css2?family=Source+Sans+3:wght@300;400;600&display=swap">
<style>
  :root {
    --paper: #ffffff;
    --page-bg: #ffffff;
    --ink: #1e1e1e;
    --ink-soft: #2b2b2b;
    --mint: #86e6cc;
    --mint-text: #8fe3d0;
    --brand-grey: #555a5c;
    --band: #7fd3c0;
    --trim: #b9b9b9;
    --photo-light: #b9e07a;
    --photo-mid: #5f9e2c;
    --photo-dark: #2f5f1a;
  }
  * { box-sizing: border-box; margin: 0; padding: 0; }
  html, body {
    width: 1200px; height: 1172px; overflow: hidden;
    background: var(--page-bg);
    font-family: "Source Sans 3", sans-serif;
    color: var(--ink);
  }
  .canvas { position: relative; width: 1200px; height: 1172px; }

  .panel {
    position: absolute; left: 28px; width: 1144px;
    background: var(--paper);
    border: 1px dotted var(--trim);
    box-shadow: 3px 4px 5px rgba(0,0,0,0.28);
    overflow: hidden;
  }
  .panel--front { top: 33px; height: 538px; }
  .panel--back { top: 600px; height: 540px; }

  /* front */
  .hero-photo { position: absolute; left: 37px; top: 36px; width: 624px; height: 466px; }
  .brand {
    position: absolute; left: 738px; top: 38px;
    display: flex; align-items: center; gap: 26px;
  }
  .brand__dot {
    width: 112px; height: 112px; border-radius: 50%;
    border: 6px solid var(--mint);
  }
  .brand__name {
    font-weight: 400; font-size: 27px; line-height: 32px;
    letter-spacing: 4.5px; color: var(--brand-grey); text-transform: uppercase;
  }
  .headline {
    position: absolute; right: 38px; top: 247px;
    text-align: right; font-weight: 400; font-size: 34px; line-height: 41px;
    color: var(--ink);
  }
  .tagline {
    position: absolute; right: 36px; top: 390px;
    text-align: right; font-weight: 300; font-size: 32px; line-height: 39px;
    color: var(--ink-soft);
  }

  /* back */
  .band { position: absolute; left: 0; width: 100%; height: 28px; background: var(--band); }
  .band--top { top: 0; }
  .band--bottom { bottom: 0; }

  .copy {
    position: absolute; left: 37px; top: 98px; width: 1078px;
    font-weight: 400; font-size: 20.3px; line-height: 29px; color: var(--ink-soft);
  }
  .copy p + p { margin-top: 29px; }
  .hl { color: var(--mint-text); font-size: 23.8px; font-weight: 400; }

  .contact {
    position: absolute; left: 37px; top: 443px; width: 1080px;
    display: flex; font-size: 15.6px; line-height: 20.5px; color: var(--ink);
  }
  .contact__who { width: 307px; font-weight: 400; }
  .contact__address { width: 308px; font-weight: 300; }
  .contact__phone { width: 191px; font-weight: 300; }
  .contact__phone b { font-weight: 600; display: inline-block; width: 14px; }
  .contact__web { font-weight: 300; }
</style>
</head>
<body>
<div class="canvas">

  <section class="panel panel--front">
    <svg class="hero-photo" viewBox="0 0 624 466" role="img" aria-label="Photo of a smiling mother and her toddler on a picnic rug in a sunny green park">
      <defs>
        <linearGradient id="parkGreen" x1="0" y1="0" x2="1" y2="1">
          <stop offset="0" stop-color="var(--photo-dark)"/>
          <stop offset="0.45" stop-color="var(--photo-mid)"/>
          <stop offset="1" stop-color="var(--photo-light)"/>
        </linearGradient>
      </defs>
      <path d="M40 0 H566 L624 232 L566 466 H0 V40 A40 40 0 0 1 40 0 Z" fill="url(#parkGreen)"/>
    </svg>

    <div class="brand">
      <div class="brand__dot"></div>
      <div class="brand__name">Wellmind<br>Counselling<br>Centre</div>
    </div>

    <h1 class="headline">Expert parenting advice<br>From toddlers to teens</h1>

    <p class="tagline">Parents want the best for their kids.<br>They want kids that are happy,<br>healthy and well behaved.</p>
  </section>

  <section class="panel panel--back">
    <div class="band band--top"></div>

    <div class="copy">
      <p><span class="hl">So why is it so hard?</span> Parents of toddlers, primary schoolers and teenagers alike say that they are frustrated by constant nagging, bribing and yelling, <span class="hl">they don’t know what to try next.</span> Some parents worry that their children are unhappy. Struggling at school, not making friends or coping with bigger problems.</p>
      <p><span class="hl">The good news</span> is that getting your children to behave more co-operatively doesn’t need to be difficult or mysterious. We all know that kids don’t come with manuals, but <span class="hl">there are skills every parent can learn to make parenting easier.</span> In a few sessions with a Parenting Psychologist, you will receive step by step guidance in how to talk to your children in a way that will be much more effective getting them to behave in a respectful and co-operative way around the home and in public. You will <span class="hl">learn how to help your child cope with problems they are going through.</span> They can help you reconnect with your kids so you can <span class="hl">enjoy being a parent again.</span></p>
    </div>

    <footer class="contact">
      <div class="contact__who">Dr Marcie Lindell &amp; Associates<br>Wellmind Counselling Centre</div>
      <div class="contact__address">Suite 1, 2087 Tamworth Road<br>Tamworth North&nbsp; Victoria&nbsp; 3118</div>
      <div class="contact__phone"><b>t</b> 6352 1840<br><b>f</b> 6352 1847</div>
      <div class="contact__web">info@wellmindcounsellingcentre.com.au<br>wellmindcounsellingcentre.com.au</div>
    </footer>

    <div class="band band--bottom"></div>
  </section>

</div>
</body>
</html>
```